Stickers signage for the outside of a 24 foot box truck.

This truck is for an oil field service truck, I have included a picture of the truck and the logo. The service is steam, heating and pressure washing for the oil field. Because of the large area to use for branding and advertising, I would like to have large decals placed on the truck, but not a full wrap due to the cost and the style is not what we are looking for.

I would like a series of large decals with log, phone number, email and some of the words mentioned, steam, heating, pressure washing place on. I would like some creativity in using the logo and graphics that compliment the logo. We are looking for edgy, and simplistic at the same time. Many truck wraps have so many things going on, the brand is lost. I have posted as well as example of a brand well recognized in the industry. Though I am not personally a fan of the truck design, it is well recognized instantly, and repeatable on each truck.

Given the name of the company Heron Ridge, this gives the designer some leeway in using that in the design.

Sides, front, and back all available for signage.
Updates

Please only submit one design, unless the designs are completely different. I am looking for unique designs from different designers, and on one task done here, there were numerous similar designs submitted. Thank you for your submissions, all your hard work is appreciated.

There is a company called Bryce Oilfield Solutions, they have a brand, recognizable and memorable. Very well designed. Also the task is now guaranteed.

Colors
0192cc
000000
ffffff

```html
<!DOCTYPE html>
<html lang="en">
<head>
<meta charset="utf-8">
<title>Heron Ridge – Box Truck Decals</title>
<link rel="stylesheet" href="https://fonts.googleapis.com/css2?family=Russo+One&family=Michroma&display=swap">
<style>
  :root{
    --brand-blue:#0192cc;
    --panel-blue:#37a7d8;
    --ink:#1c1c1c;
    --white:#ffffff;
    --panel:#e6e6e9;
    --panel-edge:#c9c9cd;
    --canvas:#ffffff;
  }
  *{margin:0;padding:0;box-sizing:border-box}
  html,body{width:1200px;height:1000px;overflow:hidden;background:var(--canvas)}
  .canvas{position:relative;width:1200px;height:1000px}
  .panel{position:absolute;background:var(--panel);border:1px solid var(--panel-edge);overflow:hidden}
  .brand-name{font-family:"Russo One",sans-serif;color:var(--ink);text-transform:uppercase;line-height:1;white-space:nowrap}
  .brand-sub,.services,.contact{font-family:"Michroma",sans-serif;text-transform:uppercase;white-space:nowrap}
  .brand-sub{color:var(--brand-blue)}
  .mark-square{position:absolute;background:var(--ink)}

  /* side panel */
  .side{left:475px;top:90px;width:560px;height:240px}
  .side .band{position:absolute;left:0;right:0;top:126px;bottom:0;background:var(--panel-blue)}
  .side .mark-square{left:70px;top:50px;width:120px;height:120px}
  .side .brand-name{position:absolute;left:205px;top:62px;font-size:37px;letter-spacing:.5px}
  .side .brand-sub{position:absolute;left:206px;top:100px;font-size:11.5px;letter-spacing:4.6px}
  .side .services{position:absolute;left:270px;top:142px;color:var(--white);font-size:11px;letter-spacing:3.4px;line-height:24px;list-style:none}
  .side .phone{position:absolute;left:205px;top:199px;color:var(--ink);font-size:18px;letter-spacing:3px}
  .side .web{position:absolute;left:208px;top:225px;color:var(--white);font-size:7px;letter-spacing:1px;word-spacing:12px}

  .drop{display:inline-block;width:9px;height:12px;vertical-align:-1px;margin-right:10px}

  /* front cap panel */
  .front{left:265px;top:510px;width:300px;height:105px}
  .front .mark-square{left:119px;top:34px;width:54px;height:50px}
  .front .left{position:absolute;left:31px;top:64px;font-size:21px}
  .front .right{position:absolute;left:179px;top:64px;font-size:21px}
  .front .brand-sub{position:absolute;left:62px;top:88px;font-size:6.5px;letter-spacing:2.6px}

  /* rear door panel */
  .rear{left:675px;top:522px;width:295px;height:280px}
  .rear .mark-square{left:108px;top:42px;width:85px;height:76px;border-radius:4px}
  .rear .brand-name{position:absolute;left:34px;top:131px;font-size:24px}
  .rear .brand-sub{position:absolute;left:35px;top:155px;font-size:7.5px;letter-spacing:2.8px}
  .rear .services{position:absolute;left:36px;top:183px;width:228px;display:flex;justify-content:space-between;list-style:none;font-size:5.4px;letter-spacing:.5px;color:var(--ink)}
  .rear .services li{display:flex;align-items:center}
  .rear .services .drop{width:5px;height:7px;margin-right:2px;vertical-align:0}
  .rear .phone{position:absolute;left:35px;top:209px;font-size:13px;letter-spacing:2px;color:var(--brand-blue)}
  .rear .web{position:absolute;left:35px;top:228px;font-size:5.5px;letter-spacing:.6px;word-spacing:8px;color:var(--brand-blue)}
</style>
</head>
<body>
<main class="canvas">

  <section class="panel side" aria-label="Side decal">
    <div class="band"></div>
    <div class="mark-square"></div>
    <h1 class="brand-name">Heron Ridge</h1>
    <p class="brand-sub">Oilfield Services Limited</p>
    <ul class="services">
      <li><svg class="drop" viewBox="0 0 10 14"><path d="M5 0 C5 4 9 7 9 10 A4 4 0 0 1 1 10 C1 7 5 4 5 0Z" fill="#fff"/></svg>Steam, Heating,</li>
      <li><svg class="drop" viewBox="0 0 10 14"><path d="M5 0 C5 4 9 7 9 10 A4 4 0 0 1 1 10 C1 7 5 4 5 0Z" fill="#fff"/></svg>Pressure Washing</li>
    </ul>
    <p class="contact phone">+63 (0) 555 010 246</p>
    <p class="contact web">www.heronridge.com info@heronridge.com</p>
  </section>

  <section class="panel front" aria-label="Front cap decal">
    <div class="mark-square"></div>
    <span class="brand-name left">Heron</span>
    <span class="brand-name right">Ridge</span>
    <p class="brand-sub">Oilfield Services Limited</p>
  </section>

  <section class="panel rear" aria-label="Rear door decal">
    <div class="mark-square"></div>
    <h2 class="brand-name">Heron Ridge</h2>
    <p class="brand-sub">Oilfield Services Limited</p>
    <ul class="services">
      <li><svg class="drop" viewBox="0 0 10 14"><path d="M5 0 C5 4 9 7 9 10 A4 4 0 0 1 1 10 C1 7 5 4 5 0Z" fill="#1c1c1c"/></svg>Steam</li>
      <li><svg class="drop" viewBox="0 0 10 14"><path d="M5 0 C5 4 9 7 9 10 A4 4 0 0 1 1 10 C1 7 5 4 5 0Z" fill="#1c1c1c"/></svg>Heating</li>
      <li><svg class="drop" viewBox="0 0 10 14"><path d="M5 0 C5 4 9 7 9 10 A4 4 0 0 1 1 10 C1 7 5 4 5 0Z" fill="#1c1c1c"/></svg>Pressure Washing</li>
    </ul>
    <p class="contact phone">+63 (0) 555 010 246</p>
    <p class="contact web">www.heronridge.com info@heronridge.com</p>
  </section>

</main>
</body>
</html>
```